Pina Colada Paradise, Take-a-Vacation Postcard

I'm a freelance pharmaceutical copywriter trying to attract new clients before the end of the summer vacation season. I have a creative commons stock photo already picked out, I need a skilled designer to incorporate the included copy. As far as tonality, I would like to communicate a professional and energetic mood to counter-balance the visual. A little Caribbean whimsy might be cool to carry over to the back. Please try to keep the line breaks on the front headline as is. I've indicated on the copy that my contact information must be prominent. Not used car salesman-like, but tasteful and in tone with the rest of the layout. I'm selling my ability to write, so an easy-to-read font is a priority. I like the color palate of the picture. Also: Please design according to Harlow Mail Specifications for Oversize 8.52" x 5.47" Postcard.P.S. August is right around the corner, so timing is a huge priority.
Updates
Please conform to Harlow Mail design standards for 5 1/2 x 8 1/2 postcard Added Wednesday, July 29, 2015
Target Market(s)
NYC Creative Directors
Industry/Entity Type
Pharmaceutical
Requirements
Must have
- Harlow Mail Specs for 5 1/2" x 8 1/2" Post Card (room for address, postage.)
- Prominent, but not "loud" contact information on back.
- I need to come across as polished and professional.
Nice to have
- 90% sure I want to use the visual supplied. Info in Project Description.
- (Easy-to-read copy is vital, since I'm selling my writing service). Otherwise, use your imagination.
- NEW AS OF THURS 11:00 PM: If you are unfamiliar with the requirements for the back of the postcard, try this link as a guideline. I've also posted 2 examples under Added Files. Use what I've provided as a guideline. We can make adjustments if necessary.
- http://www.quillandtandem.example/templates/mailing/5.5X8.5_Postcard.pdf
- FRI 7/31 2:20 - If you need further reference, I've added a third postcard example. This is the exact same same size as the on you are working on and conforms to the specifications I need. See uploaded file: "postcard example 3"
Should not have
- Busy layout

```html
<!DOCTYPE html>
<html lang="en">
<head>
<meta charset="utf-8">
<title>Relax! Postcard – Dorian Vell Copywriting</title>
<link rel="stylesheet" href="https://fonts.googleapis.com/css2?family=Oswald:wght@500;700&family=Open+Sans:wght@400;600;700;800&display=swap">
<style>
  :root{
    --red:#e0262f;
    --red-dark:#c51d26;
    --cyan:#29b6e3;
    --cyan-light:#7fd6f2;
    --white:#ffffff;
    --ink:#555b61;
    --stage:#e9ebee;
    --sky:#6fc3ea;
    --sea:#2aa6cf;
    --sand:#efe6d6;
  }
  *{box-sizing:border-box;margin:0;padding:0}
  html,body{width:900px;height:1200px;overflow:hidden}
  body{background:var(--stage);font-family:"Open Sans",Arial,sans-serif;position:relative}
  .postcard{position:absolute;left:40px;width:820px;height:530px;background:var(--white);overflow:hidden;box-shadow:0 4px 14px rgba(0,0,0,.18)}
  .postcard--front{top:40px}
  .postcard--back{top:630px}
  .postcard svg.shapes{position:absolute;inset:0}

  /* front */
  .front-headline{position:absolute;left:34px;top:120px;font-family:"Oswald",Impact,sans-serif;font-weight:700;font-size:92px;line-height:1;color:var(--cyan-light);letter-spacing:1px}
  .front-tagline{position:absolute;left:36px;top:232px;font-family:"Open Sans",Arial,sans-serif;font-weight:700;font-size:27px;line-height:1.32;color:var(--white)}
  .front-url{position:absolute;left:0;width:820px;top:460px;text-align:center;font-family:"Open Sans",Arial,sans-serif;font-weight:600;font-size:19px;letter-spacing:4px;color:var(--ink)}

  /* back */
  .savor-title{position:absolute;left:360px;top:26px;font-family:"Oswald",Impact,sans-serif;font-weight:500;font-size:27px;line-height:1.1;color:var(--cyan-light);text-align:right;width:200px}
  .savor-sub{position:absolute;left:330px;top:92px;width:230px;text-align:right;font-weight:700;font-size:11px;color:var(--white)}
  .stamp-box{position:absolute;left:706px;top:22px;width:88px;height:96px;border:2px dashed #b9bec4}
  .pitch{position:absolute;left:300px;top:140px;width:262px;font-size:11.5px;line-height:1.45;color:var(--ink)}
  .provide-title{position:absolute;left:36px;top:250px;font-family:"Oswald",Impact,sans-serif;font-weight:700;font-size:30px;color:var(--white)}
  .provide-list{position:absolute;left:52px;top:296px;width:230px;list-style:none;font-size:11.5px;line-height:1.4;color:var(--white)}
  .provide-list li{position:relative;padding-left:14px}
  .provide-list li::before{content:"";position:absolute;left:0;top:6px;width:5px;height:5px;border-radius:50%;background:var(--white)}
  .quality-line{position:absolute;left:30px;top:392px;font-weight:700;font-size:11.5px;color:var(--red)}
  .contact-title{position:absolute;left:30px;top:414px;font-family:"Oswald",Impact,sans-serif;font-weight:500;font-size:22px;color:var(--red);letter-spacing:.5px}
  .contact-title .contact-name{color:var(--cyan)}
  .contact-band{position:absolute;left:0;top:452px;width:400px;height:78px;background:var(--cyan);display:flex;gap:34px;padding:10px 30px;font-size:11px;line-height:1.55;color:var(--white)}
  .contact-item{display:flex;align-items:center;gap:6px}
  .contact-item svg{flex:none}
</style>
</head>
<body>

<section class="postcard postcard--front">
  <svg class="shapes" width="820" height="530" viewBox="0 0 820 530">
    <defs>
      <linearGradient id="beachFront" x1="0" y1="0" x2="0" y2="1">
        <stop offset="0" stop-color="#4fb2e6"/>
        <stop offset=".45" stop-color="#9ad6f0"/>
        <stop offset=".55" stop-color="var(--sea)"/>
        <stop offset=".68" stop-color="#e9dcc6"/>
        <stop offset="1" stop-color="var(--sand)"/>
      </linearGradient>
    </defs>
    <rect class="photo" x="300" y="0" width="520" height="440" fill="url(#beachFront)" role="img" aria-label="Beach photo with a tropical drink and palm silhouette"/>
    <path class="red-panel" d="M0 0 H470 C400 120 430 300 520 440 H0 Z" fill="var(--red)"/>
    <path class="url-band" d="M0 430 C260 410 560 420 820 440 V530 H0 Z" fill="var(--white)"/>
    <path class="accent-curve" d="M0 505 C260 490 560 495 820 515" stroke="var(--cyan)" stroke-width="3" fill="none"/>
  </svg>
  <h1 class="front-headline">RELAX!</h1>
  <p class="front-tagline">You work on the tan lines<br>I'll work on the taglines</p>
  <p class="front-url">www.dorianvell.example</p>
</section>

<section class="postcard postcard--back">
  <svg class="shapes" width="820" height="530" viewBox="0 0 820 530">
    <defs>
      <linearGradient id="beachBack" x1="0" y1="0" x2="0" y2="1">
        <stop offset="0" stop-color="#5db8e6"/>
        <stop offset=".5" stop-color="#a7dcef"/>
        <stop offset=".62" stop-color="var(--sea)"/>
        <stop offset=".75" stop-color="#e6d8c0"/>
        <stop offset="1" stop-color="var(--sand)"/>
      </linearGradient>
    </defs>
    <rect class="photo" x="0" y="0" width="290" height="290" fill="url(#beachBack)" role="img" aria-label="Palm tree over a sunny beach"/>
    <path class="savor-band" d="M250 10 H570 V120 H300 C320 90 300 50 250 10 Z" fill="var(--red)"/>
    <path class="provide-panel" d="M0 240 C90 215 200 225 300 200 C285 270 290 330 300 380 H0 Z" fill="var(--red)"/>
    <path class="accent-curve" d="M0 238 C90 212 200 222 302 196" stroke="var(--cyan)" stroke-width="3" fill="none"/>
  </svg>
  <h2 class="savor-title">SAVOR THE REST OF THE SUMMER</h2>
  <p class="savor-sub">With stress-free freelance copy</p>
  <div class="stamp-box" aria-hidden="true"></div>
  <p class="pitch">I possess a rare combination of pharma copy expertise and seaside sense. As such, I can assure you that now is the perfect time to stop waiting and start chilling.</p>
  <h3 class="provide-title">I PROVIDE:</h3>
  <ul class="provide-list">
    <li>First rate, first draft copy</li>
    <li>Pharma instincts with a creative soul</li>
    <li>15 years of senior-level experience</li>
    <li>The battle-tested ability to shoulder a heavy workload</li>
  </ul>
  <p class="quality-line">I'll put in the quality work so you can have some quality time.</p>
  <p class="contact-title">CONTACT <span class="contact-name">DORIAN VELL</span> TODAY:</p>
  <div class="contact-band">
    <div class="contact-col">
      <div class="contact-item">
        <svg width="10" height="10" viewBox="0 0 10 10"><path d="M2 1 L4 1 L4.6 3 L3.4 3.8 C4 5.2 4.8 6 6.2 6.6 L7 5.4 L9 6 V8 C9 8.6 8.6 9 8 9 C4.2 9 1 5.8 1 2 C1 1.4 1.4 1 2 1 Z" fill="var(--white)"/></svg>
        <span>555-014-2290</span>
      </div>
      <div class="contact-item">
        <svg width="10" height="10" viewBox="0 0 10 10"><rect x="0.5" y="2" width="9" height="6" fill="none" stroke="var(--white)"/><path d="M0.5 2 L5 5.5 L9.5 2" fill="none" stroke="var(--white)"/></svg>
        <span>hello@dorianvell.example</span>
      </div>
      <div class="contact-item">
        <svg width="10" height="10" viewBox="0 0 10 10"><circle cx="5" cy="5" r="4" fill="none" stroke="var(--white)"/></svg>
        <span>www.dorianvell.example</span>
      </div>
    </div>
    <div class="contact-col">
      <div class="contact-item">
        <svg width="10" height="10" viewBox="0 0 10 10"><path d="M5 9.5 C2.5 6.5 1.5 5 1.5 3.6 A3.5 3.5 0 0 1 8.5 3.6 C8.5 5 7.5 6.5 5 9.5 Z" fill="var(--white)"/></svg>
        <span>Dorian Vell</span>
      </div>
      <div>48 Larkspur Ave, Suite 2</div>
      <div>Brookhaven 00000</div>
    </div>
  </div>
</section>

</body>
</html>
```